Graphic Design Set for Banner Ads - Sizes and Specs for Pixmora

We need a set of 6 ads of the following sizes created for Pixmora:

Medium rectangle: 300×250
Leaderboard: 728×90
Wide skyscraper: 160×600
Large rectangle: 300x600
Mobile leaderboard: 320×50

Here are the Formatting Guidelines (WEB ADS): https://help.pixmora.example/hc/en-us/articles/583920147-Ad-Content-and-Format-Guidelines

Here is the website: https://valmiraliving.example/

Here are some words for the ad - feel free to use creative liberties if you have something better or need less words.

1. The Future of Aging is Here

2. Dementia At-Home Care

3. Benefits of an Assisted Living from the Privacy of Your Home - link to

4. Idaho's New Senior Care Option

5. The Security of Senior Living from the Comfort of Your Home

I have the images for all website photos, if you need more images, please let me know.

Target Market(s)

Women age 55+

Industry/Entity Type

Graphic Design

Requirements
Must have
• Incorporate website imagery as much as possible
Should not have
• a feeling of helplessness, old, etc.

```html
<!DOCTYPE html>
<html lang="en">
<head>
<meta charset="utf-8">
<title>Valmira Living – Banner Ad Set</title>
<link href="https://fonts.googleapis.com/css2?family=Mulish:wght@400;700;800&family=Oswald:wght@300;400&display=swap" rel="stylesheet">
<style>
:root{
  --backdrop:#2d2d2d;
  --ink:#222222;
  --gold:#b8902f;
  --gold-light:#d9b65a;
  --silver-top:#ffffff;
  --silver-bottom:#d6d6d6;
  --bar:#6a6a6a;
  --button:#1f1f1f;
  --photo-a:#f2d6b3;
  --photo-b:#c98c66;
  --photo-c:#6f7a52;
}
*{box-sizing:border-box;margin:0;padding:0}
html,body{width:1200px;height:1200px;overflow:hidden;background:var(--backdrop)}
body{position:relative;font-family:"Mulish",sans-serif;color:var(--ink)}
.ad{position:absolute;overflow:hidden;background:linear-gradient(180deg,var(--silver-top),var(--silver-bottom));box-shadow:0 4px 10px rgba(0,0,0,.55)}
.photo{position:absolute;left:0;top:0;background:linear-gradient(135deg,var(--photo-a) 0%,var(--photo-b) 55%,var(--photo-c) 100%)}
.swoosh{position:absolute;left:0;width:100%}
.headline{position:absolute;font-weight:800;line-height:1.15;text-align:center}
.perks{position:absolute;list-style:none;font-family:"Oswald",sans-serif;font-weight:300;line-height:1.1}
.perks .gold{color:var(--gold);font-weight:400}
.perks li{position:relative}
.tick{position:absolute;left:0}
.brand{position:absolute;font-family:"Mulish",sans-serif;font-weight:400;color:var(--ink);line-height:1;letter-spacing:.04em;display:flex;align-items:center;gap:6px}
.brand .dot{border:2px solid var(--gold);border-radius:50%;flex:none}
.cta{position:absolute;background:var(--button);color:#fff;font-weight:700;display:flex;align-items:center;justify-content:center;letter-spacing:.02em}
.url{position:absolute;color:var(--gold);font-weight:700;text-align:center}
.bar{position:absolute;left:0;bottom:0;width:100%;background:var(--bar)}
.rule{position:absolute;height:1px;background:#c9c9c9}
</style>
</head>
<body>

<!-- Large rectangle 300x600 -->
<section class="ad" style="left:194px;top:178px;width:300px;height:600px">
  <div class="photo" role="img" aria-label="Seniors sharing a sunny outdoor meal" style="width:300px;height:260px"></div>
  <svg class="swoosh" style="top:220px;height:50px" viewBox="0 0 300 50" preserveAspectRatio="none">
    <path d="M0 22 Q150 50 300 0 L300 50 L0 50Z" fill="#fafafa"/>
    <path d="M0 22 Q150 50 300 0" fill="none" stroke="var(--gold)" stroke-width="4"/>
  </svg>
  <h2 class="headline" style="left:10px;width:280px;top:300px;font-size:21px">The Security of<br>Senior Living from the<br>Comfort of Your Home</h2>
  <div class="rule" style="left:60px;width:180px;top:386px"></div>
  <ul class="perks" style="left:36px;top:402px;font-size:19px">
    <li style="padding-left:26px"><svg class="tick" width="20" height="18" viewBox="0 0 20 18"><rect x="1" y="4" width="12" height="12" fill="none" stroke="var(--gold)" stroke-width="1.5"/><path d="M4 9l4 4 10-12" fill="none" stroke="var(--gold)" stroke-width="2"/></svg>AT-HOME ASSISTANCE<br><span class="gold">ASSISTANCE MEMBERSHIP</span></li>
    <li style="padding-left:26px;margin-top:6px"><svg class="tick" width="20" height="18" viewBox="0 0 20 18"><rect x="1" y="4" width="12" height="12" fill="none" stroke="var(--gold)" stroke-width="1.5"/><path d="M4 9l4 4 10-12" fill="none" stroke="var(--gold)" stroke-width="2"/></svg>AT-HOME MEMORY CARE<br><span class="gold">MEMORY MEMBERSHIP</span></li>
  </ul>
  <div class="brand" style="left:16px;top:524px;font-size:22px"><span class="dot" style="width:14px;height:14px"></span>VALMIRA<br>LIVING</div>
  <a class="cta" style="left:151px;top:519px;width:139px;height:36px;font-size:16px">LEARN MORE</a>
  <div class="url" style="left:151px;width:139px;top:558px;font-size:14px">valmiraliving.example</div>
  <div class="bar" style="height:13px"></div>
</section>

<!-- Wide skyscraper 160x600 -->
<section class="ad" style="left:518px;top:178px;width:160px;height:600px">
  <div class="photo" role="img" aria-label="Seniors sharing a sunny outdoor meal" style="width:160px;height:265px"></div>
  <svg class="swoosh" style="top:225px;height:45px" viewBox="0 0 160 45" preserveAspectRatio="none">
    <path d="M0 20 Q80 45 160 0 L160 45 L0 45Z" fill="#fafafa"/>
    <path d="M0 20 Q80 45 160 0" fill="none" stroke="var(--gold)" stroke-width="4"/>
  </svg>
  <h2 class="headline" style="left:4px;width:152px;top:279px;font-size:17.5px">The Security<br>of Senior Living<br>from the Comfort<br>of Your Home</h2>
  <ul class="perks" style="left:4px;width:152px;top:378px;font-size:14px;text-align:center">
    <li>AT-HOME ASSISTANCE<br><span class="gold">ASSISTANCE MEMBERSHIP</span></li>
    <li style="margin-top:5px">AT-HOME MEMORY CARE<br><span class="gold">MEMORY MEMBERSHIP</span></li>
  </ul>
  <div class="rule" style="left:20px;width:120px;top:370px"></div>
  <div class="brand" style="left:22px;top:464px;font-size:20px;justify-content:center"><span class="dot" style="width:12px;height:12px"></span>VALMIRA<br>LIVING</div>
  <a class="cta" style="left:11px;top:518px;width:139px;height:36px;font-size:15px">LEARN MORE</a>
  <div class="url" style="left:0;width:160px;top:560px;font-size:13px">valmiraliving.example</div>
  <div class="bar" style="height:12px"></div>
</section>

<!-- Medium rectangle 336x280 -->
<section class="ad" style="left:703px;top:223px;width:336px;height:280px">
  <div class="photo" role="img" aria-label="Seniors sharing a sunny outdoor meal" style="width:336px;height:128px"></div>
  <svg class="swoosh" style="top:70px;height:60px" viewBox="0 0 336 60" preserveAspectRatio="none">
    <path d="M0 52 Q200 60 336 0 L336 60 L0 60Z" fill="#fafafa"/>
    <path d="M0 52 Q200 60 336 0" fill="none" stroke="var(--gold)" stroke-width="4"/>
  </svg>
  <h2 class="headline" style="left:12px;top:137px;font-size:22px;text-align:left">The Future of Aging is Here</h2>
  <ul class="perks" style="left:14px;top:168px;font-size:16px">
    <li style="padding-left:20px"><svg class="tick" width="17" height="15" viewBox="0 0 20 18"><rect x="1" y="4" width="12" height="12" fill="none" stroke="var(--gold)" stroke-width="1.5"/><path d="M4 9l4 4 10-12" fill="none" stroke="var(--gold)" stroke-width="2"/></svg>AT-HOME ASSISTANCE <span class="gold">ASSISTANCE MEMBERSHIP</span></li>
    <li style="padding-left:20px;margin-top:2px"><svg class="tick" width="17" height="15" viewBox="0 0 20 18"><rect x="1" y="4" width="12" height="12" fill="none" stroke="var(--gold)" stroke-width="1.5"/><path d="M4 9l4 4 10-12" fill="none" stroke="var(--gold)" stroke-width="2"/></svg>AT-HOME MEMORY CARE <span class="gold">MEMORY MEMBERSHIP</span></li>
  </ul>
  <div class="brand" style="left:22px;top:222px;font-size:20px"><span class="dot" style="width:13px;height:13px"></span>VALMIRA<br>LIVING</div>
  <a class="cta" style="left:179px;top:220px;width:139px;height:35px;font-size:15px">LEARN MORE</a>
  <div class="url" style="left:179px;width:139px;top:257px;font-size:13px">valmiraliving.example</div>
  <div class="bar" style="height:7px"></div>
</section>

<!-- Medium rectangle 300x250 -->
<section class="ad" style="left:703px;top:528px;width:300px;height:250px">
  <div class="photo" role="img" aria-label="Seniors sharing a sunny outdoor meal" style="width:300px;height:114px"></div>
  <svg class="swoosh" style="top:62px;height:54px" viewBox="0 0 300 54" preserveAspectRatio="none">
    <path d="M0 47 Q180 54 300 0 L300 54 L0 54Z" fill="#fafafa"/>
    <path d="M0 47 Q180 54 300 0" fill="none" stroke="var(--gold)" stroke-width="4"/>
  </svg>
  <h2 class="headline" style="left:11px;top:123px;font-size:19.5px;text-align:left">The Future of Aging is Here</h2>
  <ul class="perks" style="left:12px;top:150px;font-size:14px">
    <li style="padding-left:18px"><svg class="tick" width="15" height="13" viewBox="0 0 20 18"><rect x="1" y="4" width="12" height="12" fill="none" stroke="var(--gold)" stroke-width="1.5"/><path d="M4 9l4 4 10-12" fill="none" stroke="var(--gold)" stroke-width="2"/></svg>AT-HOME ASSISTANCE <span class="gold">ASSISTANCE MEMBERSHIP</span></li>
    <li style="padding-left:18px;margin-top:2px"><svg class="tick" width="15" height="13" viewBox="0 0 20 18"><rect x="1" y="4" width="12" height="12" fill="none" stroke="var(--gold)" stroke-width="1.5"/><path d="M4 9l4 4 10-12" fill="none" stroke="var(--gold)" stroke-width="2"/></svg>AT-HOME MEMORY CARE <span class="gold">MEMORY MEMBERSHIP</span></li>
  </ul>
  <div class="brand" style="left:20px;top:196px;font-size:18px"><span class="dot" style="width:12px;height:12px"></span>VALMIRA<br>LIVING</div>
  <a class="cta" style="left:160px;top:195px;width:124px;height:32px;font-size:14px">LEARN MORE</a>
  <div class="url" style="left:160px;width:124px;top:229px;font-size:11px">valmiraliving.example</div>
  <div class="bar" style="height:5px"></div>
</section>

<!-- Leaderboard 728x90 -->
<section class="ad" style="left:194px;top:802px;width:728px;height:90px">
  <div class="photo" role="img" aria-label="Seniors sharing a sunny outdoor meal" style="width:210px;height:90px"></div>
  <svg style="position:absolute;left:170px;top:0;width:60px;height:90px" viewBox="0 0 60 90" preserveAspectRatio="none">
    <path d="M15 0 Q50 45 30 90 L60 90 L60 0Z" fill="#f4f4f4"/>
    <path d="M15 0 Q50 45 30 90" fill="none" stroke="var(--gold)" stroke-width="4"/>
  </svg>
  <div class="brand" style="left:228px;top:24px;font-size:24px"><span class="dot" style="width:15px;height:15px"></span>VALMIRA<br>LIVING</div>
  <h2 class="headline" style="left:371px;top:16px;font-size:16px;text-align:left;line-height:1.33">The Security of<br>Senior Living from the<br>Comfort of Your Home</h2>
  <a class="cta" style="left:569px;top:21px;width:139px;height:37px;font-size:16px">LEARN MORE</a>
  <div class="url" style="left:569px;width:139px;top:61px;font-size:14px">valmiraliving.example</div>
</section>

<!-- Mobile leaderboard 320x50 -->
<section class="ad" style="left:198px;top:916px;width:320px;height:50px">
  <div class="photo" role="img" aria-label="Seniors sharing a sunny outdoor meal" style="width:100px;height:50px"></div>
  <svg style="position:absolute;left:88px;top:0;width:22px;height:50px" viewBox="0 0 22 50" preserveAspectRatio="none">
    <path d="M4 0 Q18 25 8 50 L22 50 L22 0Z" fill="#f4f4f4"/>
    <path d="M4 0 Q18 25 8 50" fill="none" stroke="var(--gold)" stroke-width="2.5"/>
  </svg>
  <h2 class="headline" style="left:116px;top:8px;font-size:9.5px;text-align:left;line-height:1.25">The Security of<br>Senior Living from the<br>Comfort of Your Home</h2>
  <div class="brand" style="left:250px;top:4px;font-size:11px">VALMIRA</div>
  <a class="cta" style="left:236px;top:26px;width:78px;height:19px;font-size:8.5px">LEARN MORE</a>
</section>

</body>
</html>
```